Website for a Party Bus charter business

Please prepare a site for a local party bus charter company names Fenwick Bus Company.
They hire a party bus, chatrer bus, boat hire and party trailer hire (place holder photos fine for these items).
I have included a wireframe design. This should be used, however creative licence is fully extended
Delivery of PSD is required and all fonts and source files
The client likes: http://www.tallpinoca.com.au/ but must not look completely the same.
Should use a gold (simualr to #D1CFA1) colour, even if just background.
Hi All, just wondering if anyone is working on this as I have not received any responses or questions?
Is there anything I can do to assist?
Thanks all for the great submissions. I will be sending these onto the client today. Will let you know the outcome as soon as I can
Business

```html
<!DOCTYPE html>
<html lang="en">
<head>
<meta charset="utf-8">
<title>Fenwick Bus Company</title>
<link href="https://fonts.googleapis.com/css2?family=Questrial&display=swap" rel="stylesheet">
<style>
:root{
  --black:#000;
  --ink:#111;
  --white:#fff;
  --gold:#d6b24c;
  --gold-dark:#b8902f;
  --gold-light:#e9d48a;
  --sand:#d6d3a2;
  --sand-dark:#c2be8a;
  --sky:#3fb4e0;
  --sky-dark:#2d8fbd;
  --muted:#555;
  --red:#d8141b;
}
*{box-sizing:border-box;margin:0;padding:0}
html,body{width:1200px;height:2384px;overflow:hidden;background:var(--white)}
body{font-family:"Questrial",sans-serif;color:var(--ink);position:relative}
.abs{position:absolute}

/* header */
.site-header{position:absolute;left:0;top:0;width:1200px;height:157px;background:var(--black)}
.brand{position:absolute;left:128px;top:58px;display:flex;align-items:center;gap:12px}
.brand-dot{width:40px;height:40px;border-radius:50%;background:var(--gold)}
.brand-name{color:var(--gold);font-size:24px}
.social-row{position:absolute;left:468px;top:16px;display:flex;gap:7px}
.social-row span{width:25px;height:25px;border-radius:50%;background:var(--white)}
.search{position:absolute;left:700px;top:13px;width:209px;height:35px;background:var(--white);border-radius:4px;color:#999;font-size:13px;padding:9px 14px}
.search svg{position:absolute;right:10px;top:8px}
.share-badges{position:absolute;left:920px;top:14px;display:grid;grid-template-columns:60px 54px;gap:5px 6px}
.share-badges span{height:14px;border-radius:2px;background:var(--white)}
.main-nav{position:absolute;top:79px;left:586px;display:flex;gap:0}
.main-nav a{display:block;color:var(--white);text-decoration:none;font-size:17px;height:40px;line-height:40px;padding:0 12px;margin-right:14px}
.main-nav a.active{background:linear-gradient(var(--gold-light),var(--gold-dark));color:var(--black);border-radius:3px;padding:0 12px}

/* category bar */
.category-bar{position:absolute;top:157px;left:0;width:1200px;height:51px;background:linear-gradient(var(--gold-light),var(--gold) 55%,var(--gold-dark));display:flex;justify-content:center;align-items:center;gap:22px;font-size:17px;color:var(--ink)}

/* slider */
.hero{position:absolute;top:208px;left:0;width:1200px;height:412px;background:var(--sand)}
.slide{position:absolute}
.slide-side-left{left:183px;top:30px;width:183px;height:358px;background:linear-gradient(135deg,#c43a7a,#3b2a6b 60%,#e0a23a);clip-path:polygon(0 0,100% 8%,100% 92%,0 100%)}
.slide-main{left:366px;top:30px;width:468px;height:356px;background:linear-gradient(160deg,#3a3550,#8a6a60 45%,#e0c27a)}
.slide-side-right{left:834px;top:30px;width:180px;height:358px;background:linear-gradient(200deg,#8a4a8a,#2a2040 55%,#b0703a);clip-path:polygon(0 8%,100% 0,100% 100%,0 92%)}
.hero-arrow{position:absolute;top:164px;width:48px;height:48px;border-radius:50%;background:rgba(120,118,80,.25);border:1px solid rgba(120,118,80,.4)}
.hero-arrow.prev{left:89px}.hero-arrow.next{left:1050px}
.hero-arrow svg{position:absolute;left:16px;top:14px}

/* fleet tabs */
.fleet-tabs{position:absolute;top:620px;left:0;width:1200px;height:71px;background:var(--sand-dark)}
.fleet-tabs span{position:absolute;top:0;height:71px;line-height:71px;font-size:21px;color:var(--ink)}
.fleet-tabs span.active{left:172px;width:132px;text-align:center;background:linear-gradient(var(--gold-light),var(--gold));color:#7a6632}
.fleet-tabs i{position:absolute;top:16px;width:1px;height:38px;background:rgba(0,0,0,.12)}

/* intro */
.section-title{font-size:21px;color:var(--ink)}
.section-sub{font-size:13px;color:var(--muted)}
.card-photo{position:absolute;width:113px;height:104px;background:linear-gradient(135deg,#e8e8ee,#6a6a88 55%,#2a2a3a)}
.card-photo.mono{background:linear-gradient(135deg,#eee,#888 55%,#222)}
.card-title{position:absolute;font-size:19px;color:var(--ink)}
.card-text{position:absolute;width:295px;font-size:13px;line-height:17px}
.btn-dark{position:absolute;background:var(--black);color:var(--gold);border-radius:4px;text-align:center;font-size:14px}
.btn-read{width:94px;height:33px;line-height:33px}

/* video */
.video{position:absolute;left:99px;top:1128px;width:999px;height:382px;background:radial-gradient(circle at 60% 55%,#7a7090,#3a2a6a 40%,#1a1230 80%)}
.play{position:absolute;left:457px;top:148px;width:86px;height:64px;background:var(--red);border-radius:4px}
.play svg{position:absolute;left:30px;top:18px}

/* coast */
.coast-photo{position:absolute;left:99px;top:1598px;width:427px;height:269px;background:linear-gradient(180deg,#9aa0b0,#c8ccd6 40%,#707680 75%,#4a4e55)}
.coast-text{position:absolute;left:555px;width:526px;font-size:13.5px;line-height:17.5px}
.btn-book{left:562px;top:1816px;width:132px;height:43px;line-height:43px;font-size:16px}

/* follow band */
.follow-band{position:absolute;left:0;top:1912px;width:1200px;height:130px;background:var(--sky);color:var(--white);text-align:center}
.follow-band .mark{position:absolute;left:577px;top:28px;width:46px;height:46px;border-radius:50%;background:var(--white)}
.follow-band p{position:absolute;left:0;width:1200px;top:88px;font-size:16px}
.band-arrow{position:absolute;top:61px;width:29px;height:29px;background:var(--sky-dark)}
.band-arrow svg{position:absolute;left:9px;top:8px}

/* footer columns */
.col-title{position:absolute;top:2058px;font-size:21px}
.small{position:absolute;font-size:13px;line-height:17px}
.thumb{position:absolute;width:80px;height:73px;background:linear-gradient(135deg,#d9c79a,#3a3030 60%,#111)}
.thumb.mono{background:linear-gradient(135deg,#ddd,#555 60%,#111)}
.field{position:absolute;left:787px;width:233px;height:34px;border:1px solid #bbb;border-radius:5px;background:#eee;font-size:12px;color:#666;padding:8px 12px}
.btn-wide{height:35px;line-height:35px;font-size:19px}

/* bottom bar */
.site-footer{position:absolute;left:0;top:2304px;width:1200px;height:80px;background:var(--black)}
.copyright{position:absolute;left:105px;top:30px;color:var(--gold);font-size:12px}
.foot-social{position:absolute;left:857px;top:17px;display:flex;gap:7px}
.foot-social span{width:24px;height:24px;border-radius:50%;background:var(--white)}
.legal{position:absolute;left:918px;top:55px;color:var(--gold);font-size:13px}
</style>
</head>
<body>

<header class="site-header">
  <div class="brand"><span class="brand-dot"></span><span class="brand-name">Fenwick Bus Company</span></div>
  <div class="social-row"><span></span><span></span><span></span><span></span><span></span><span></span><span></span></div>
  <div class="search">Search
    <svg width="18" height="18" viewBox="0 0 18 18"><circle cx="7" cy="7" r="5.5" fill="none" stroke="#999" stroke-width="2"/><line x1="11" y1="11" x2="16.5" y2="16.5" stroke="#999" stroke-width="2.5"/></svg>
  </div>
  <div class="share-badges"><span></span><span></span><span></span><span></span></div>
  <nav class="main-nav">
    <a class="active" href="#">Home</a><a href="#">Vehicles</a><a href="#">Gallery</a><a href="#">Get a Quote</a><a href="#">Contact Us</a>
  </nav>
</header>

<nav class="category-bar">
  <span>Transport</span><span>Party Bus</span><span>Charter Bus</span><span>Formals</span><span>Events Transfers</span><span>Christmas Party</span><span>Team Building Day</span>
</nav>

<section class="hero">
  <div class="slide slide-side-left" role="img" aria-label="Friends dancing with cocktails at a party"></div>
  <div class="slide slide-main" role="img" aria-label="Group of women laughing and dancing on a party bus"></div>
  <div class="slide slide-side-right" role="img" aria-label="Guests toasting with a chauffeur on board"></div>
  <span class="hero-arrow prev"><svg width="14" height="20" viewBox="0 0 14 20"><polyline points="11,2 3,10 11,18" fill="none" stroke="#555" stroke-width="2"/></svg></span>
  <span class="hero-arrow next"><svg width="14" height="20" viewBox="0 0 14 20"><polyline points="3,2 11,10 3,18" fill="none" stroke="#555" stroke-width="2"/></svg></span>
</section>

<nav class="fleet-tabs">
  <span class="active">Party Bus</span>
  <span style="left:327px">Charter Bus</span><i style="left:452px"></i>
  <span style="left:464px">Party Trailer</span><i style="left:595px"></i>
  <span style="left:609px">Party Boat</span><i style="left:722px"></i>
  <span style="left:736px">House Bus</span><i style="left:847px"></i>
  <span style="left:861px">Want You Own ?</span>
</nav>

<section class="intro">
  <h2 class="section-title abs" style="left:140px;top:714px">Fenwick Bus Company</h2>
  <p class="section-sub abs" style="left:140px;top:746px">Fun , Convientient and Some sort of catchy text</p>

  <div class="card-photo" style="left:141px;top:787px" role="img" aria-label="Cocktail glass with olives"></div>
  <h3 class="card-title" style="left:267px;top:786px">LORIUM IPSUM</h3>
  <p class="card-text" style="left:267px;top:816px">Sed ut perspiciatis unde omnis iste natus error sit voluptatem accusantium doloremque laudan- tium, totam rem aperiam, eaque ipsa quae ab illo inventore veritatis</p>
  <a class="btn-dark btn-read" style="left:459px;top:893px">Read more</a>

  <div class="card-photo mono" style="left:640px;top:787px" role="img" aria-label="Cocktail glass with olives"></div>
  <h3 class="card-title" style="left:764px;top:786px">LORIUM IPSUM</h3>
  <p class="card-text" style="left:764px;top:816px">Sed ut perspiciatis unde omnis iste natus error sit voluptatem accusantium doloremque laudan- tium, totam rem aperiam, eaque ipsa quae ab illo inventore veritatis</p>
  <a class="btn-dark btn-read" style="left:957px;top:893px">Read more</a>

  <div class="card-photo mono" style="left:141px;top:947px" role="img" aria-label="Cocktail glass with olives"></div>
  <h3 class="card-title" style="left:267px;top:946px">LORIUM IPSUM</h3>
  <p class="card-text" style="left:267px;top:976px">Sed ut perspiciatis unde omnis iste natus error sit voluptatem accusantium doloremque laudan- tium, totam rem aperiam, eaque ipsa quae ab illo inventore veritatis</p>
  <a class="btn-dark btn-read" style="left:459px;top:1054px">Read more</a>

  <div class="card-photo mono" style="left:644px;top:930px" role="img" aria-label="Cocktail glass with olives"></div>
  <h3 class="card-title" style="left:769px;top:928px">LORIUM IPSUM</h3>
  <p class="card-text" style="left:769px;top:958px">Sed ut perspiciatis unde omnis iste natus error sit voluptatem accusantium doloremque laudan- tium, totam rem aperiam, eaque ipsa quae ab illo inventore veritatis</p>
  <a class="btn-dark btn-read" style="left:961px;top:1035px">Read more</a>
</section>

<div class="video" role="img" aria-label="DJ headphones on a mixing desk under purple club lights">
  <span class="play"><svg width="28" height="28" viewBox="0 0 28 28"><polygon points="2,0 26,14 2,28" fill="#fff"/></svg></span>
</div>

<section class="coast">
  <h2 class="section-title abs" style="left:99px;top:1530px">Best way to see the coast</h2>
  <p class="section-sub abs" style="left:99px;top:1563px">Fun , Convientient and Some sort of catchy text</p>
  <div class="coast-photo" role="img" aria-label="Two coaches parked in front of snowy mountains"></div>
  <h3 class="abs" style="left:555px;top:1595px;font-size:21px;font-weight:400">Best way to see the coast</h3>
  <p class="coast-text" style="top:1637px">Sed ut perspiciatis unde omnis iste natus error sit voluptatem accusantium doloremque laudantium, totam rem aperiam, eaque ipsa quae ab illo inventore veritatis et quasi architecto beatae vitae dicta sunt explicabo. Nemo enim ipsam voluptatem quia voluptas sit aspernatur aut odit aut fugit, sed quia consequuntur magni dolores eos qui ratione voluptatem sequi nesciunt.</p>
  <p class="coast-text" style="top:1744px">Neque porro quisquam est, qui dolorem ipsum quia dolor sit amet, consectetur, adipisci velit, sed quia non numquam eius modi tempora incidunt ut labore et dolore magnam aliquam quaerat voluptatem. Ut enim ad minima</p>
  <a class="btn-dark btn-book">BOOK IT NOW</a>
</section>

<section class="follow-band">
  <span class="mark"></span>
  <p>Just now Follow @ Chirpline</p>
  <span class="band-arrow" style="left:111px"><svg width="10" height="13" viewBox="0 0 10 13"><polyline points="8,1 2,6.5 8,12" fill="none" stroke="#fff" stroke-width="2"/></svg></span>
  <span class="band-arrow" style="left:941px"><svg width="10" height="13" viewBox="0 0 10 13"><polyline points="2,1 8,6.5 2,12" fill="none" stroke="#fff" stroke-width="2"/></svg></span>
</section>

<section class="footer-columns">
  <h3 class="col-title" style="left:105px;font-weight:400">Quoting &amp; Booking</h3>
  <div class="card-photo" style="left:106px;top:2099px" role="img" aria-label="Cocktail glass with olives"></div>
  <h4 class="card-title" style="left:232px;top:2099px;font-weight:400">LORIUM IPSUM</h4>
  <p class="small" style="left:232px;top:2129px;width:180px">Sed ut perspiciatis unde omnis iste natus error sit voluptatem accusantium doloremque laudantium.</p>
  <a class="btn-dark btn-wide" style="left:151px;top:2223px;width:173px">GET A QUOTE</a>

  <h3 class="col-title" style="left:456px;font-weight:400">Latest Post</h3>
  <div class="thumb" style="left:454px;top:2098px" role="img" aria-label="Party guest portrait"></div>
  <p class="small" style="left:551px;top:2101px;width:190px">Sed ut perspiciatis unde omnis iste natus error sit voluptatem accusantium doloremque laudantium.</p>
  <div class="thumb mono" style="left:454px;top:2188px" role="img" aria-label="Party guest portrait in black and white"></div>
  <p class="small" style="left:551px;top:2191px;width:190px">Sed ut perspiciatis unde omnis iste natus error sit voluptatem accusantium doloremque laudantium.</p>

  <h3 class="col-title" style="left:787px;font-weight:400">Join Our VIP CLUB</h3>
  <p class="small" style="left:787px;top:2090px;width:245px">Sed ut perspiciatis unde omnis iste natus error sit voluptatem accusantium doloremque laudantium.</p>
  <div class="field" style="top:2151px">Name</div>
  <div class="field" style="top:2193px">Email</div>
  <a class="btn-dark btn-wide" style="left:807px;top:2239px;width:192px">JOIN OUR VIP CLUB</a>
</section>

<footer class="site-footer">
  <p class="copyright">© 2014.www.companyname.com</p>
  <div class="foot-social"><span></span><span></span><span></span><span></span><span></span></div>
  <p class="legal">Privacy | Policy</p>
</footer>

</body>
</html>
```